OTRV - Immigration and Business Consulting Marketing Brochure

81/2 x 11 tri-fold brochure or 11 x 17 tri-fold brochure which ever is suitable to display all our content. Full-colour 4/4,
Immigration and Business Consulting
Present services we provide and web-sites associated with our business. 1st page needs a picture of something related to the first step (choice of picture for your option). Logo would also need to be on this page and contact information page (Logo is uploaded) Uploaded file has all information that we would desire in our brochure. Each section is labeled for your convenience.

Please visit our primary website if you need further information - www.otrv.ca

Target Market(s)

B2B Employers needing Recruitment/Immigration assistance and foreign clients looking to immigrate to Canada.

Industry/Entity Type

Business

Font styles to use
Serif

Requirements
Must have
• Company Logo
Nice to have
• Pictures for specific areas and sections of brochure
Should not have
• Profanity/sexual explicit photos

```html
<!DOCTYPE html>
<html lang="en">
<head>
<meta charset="utf-8">
<title>OTRV – Brochure</title>
<link href="https://fonts.googleapis.com/css2?family=Lato:ital,wght@0,400;0,700;1,700&family=Oswald:wght@500&display=swap" rel="stylesheet">
<style>
  :root {
    --page-bg: #e8e5e0;
    --navy: #1d3f73;
    --blue: #1a63b8;
    --blue-deep: #0e3f86;
    --red: #d81e4a;
    --ink: #333;
    --grey: #cfd3d8;
    --white: #fff;
  }
  * { box-sizing: border-box; margin: 0; padding: 0; }
  html, body { width: 1200px; height: 907px; overflow: hidden; }
  body { background: var(--page-bg); font-family: "Lato", sans-serif; position: relative; }

  .spread {
    position: absolute; left: 210px; top: 176px;
    width: 780px; height: 555px;
    background: var(--white);
    box-shadow: 0 4px 14px rgba(0,0,0,.25);
  }
  .panel { position: absolute; top: 0; height: 555px; overflow: hidden; }
  .panel--inner { left: 0; width: 522px; }
  .panel--cover { left: 522px; width: 258px; border-left: 1px solid #ddd; }
  .art { position: absolute; inset: 0; }

  .portal-mark { position: absolute; left: 22px; top: 24px; color: var(--white); }
  .portal-mark__name { display: flex; align-items: center; gap: 5px; font-weight: 700; font-size: 13px; }
  .portal-mark__name::before { content: ""; width: 11px; height: 11px; background: var(--red); border-radius: 50%; }
  .portal-mark__tag { font-size: 5.5px; margin-top: 3px; }
  .portal-mark__note { font-size: 5px; margin-top: 3px; opacity: .9; }

  .about { position: absolute; left: 17px; top: 136px; width: 248px; }
  .about__title { font-weight: 400; font-size: 14px; color: #222; margin-bottom: 14px; }
  .about p { font-size: 7.4px; line-height: 1.28; color: var(--ink); text-align: justify; margin-bottom: 5px; }
  .about__visit { position: absolute; left: 0; top: 232px; width: 248px; text-align: center; font-size: 14px; color: var(--blue); }

  .brand { font-weight: 700; color: var(--navy); letter-spacing: 1px; display: flex; align-items: center; justify-content: center; gap: 6px; font-size: 34px; }
  .brand::before { content: ""; width: 12px; height: 12px; border-radius: 50%; background: var(--navy); }
  .brand--mid { position: absolute; left: 290px; width: 210px; top: 222px; }
  .brand--cover { position: absolute; left: 0; width: 258px; top: 58px; }

  .contact { position: absolute; left: 291px; top: 292px; width: 222px; }
  .contact__title { font-size: 12.5px; font-weight: 700; line-height: 1.3; color: var(--blue-deep); }
  .contact__list { list-style: none; margin-top: 30px; font-size: 10.5px; color: #333; }
  .contact__list li { display: flex; align-items: flex-start; gap: 6px; margin-bottom: 6px; line-height: 1.25; }
  .contact__list svg { flex: none; margin-top: 1px; }
  .contact__phones { gap: 16px !important; }
  .contact__phones span { display: flex; gap: 6px; align-items: center; }

  .links { position: absolute; left: 282px; top: 490px; width: 235px; list-style: none; display: grid; grid-template-columns: auto auto; row-gap: 7px; column-gap: 14px; color: var(--white); font-size: 10px; font-weight: 700; }
  .links li { display: flex; align-items: center; gap: 5px; }
  .links li::before { content: ""; width: 7px; height: 7px; border-radius: 50%; background: rgba(255,255,255,.85); }
  .links li.wide { grid-column: 1 / 3; }

  .cover-copy { position: absolute; left: 0; top: 428px; width: 258px; text-align: center; color: var(--white); }
  .cover-copy__title { font-family: "Oswald", sans-serif; font-weight: 500; font-size: 25px; letter-spacing: .3px; }
  .cover-copy__sub { font-style: italic; font-weight: 700; font-size: 15px; line-height: 1.4; margin-top: 2px; text-align: left; padding-left: 20px; }
  .cover-copy__url { margin-top: 14px; font-size: 11px; letter-spacing: 3px; }
</style>
</head>
<body>
<main class="spread">

  <section class="panel panel--inner">
    <svg class="art" width="522" height="555" viewBox="0 0 522 555">
      <defs>
        <linearGradient id="topBand" x1="0" y1="0" x2="1" y2="0">
          <stop offset="0" stop-color="#2a7fd8"/>
          <stop offset=".55" stop-color="#1a5aa8"/>
          <stop offset="1" stop-color="#0b2c5e"/>
        </linearGradient>
        <linearGradient id="bottomBand" x1="0" y1="0" x2="1" y2="0">
          <stop offset="0" stop-color="#0e3f86"/>
          <stop offset="1" stop-color="#2f7fd6"/>
        </linearGradient>
        <linearGradient id="redBand" x1="0" y1="0" x2="1" y2="0">
          <stop offset="0" stop-color="#b3153b"/>
          <stop offset="1" stop-color="#e02553"/>
        </linearGradient>
        <linearGradient id="globePhoto" x1="0" y1="0" x2="1" y2="1">
          <stop offset="0" stop-color="#c9ced6"/>
          <stop offset=".5" stop-color="#3a5f98"/>
          <stop offset="1" stop-color="#d58a4a"/>
        </linearGradient>
      </defs>
      <g role="img" aria-label="Businessman touching a digital network of contact icons">
        <path d="M0 0 H522 V232 C450 150 330 92 170 88 C100 86 45 92 0 100 Z" fill="url(#topBand)"/>
      </g>
      <path d="M0 100 C45 92 100 86 170 88 C330 92 450 150 522 232" fill="none" stroke="var(--red)" stroke-width="7"/>
      <path d="M0 108 C45 100 100 95 170 97 C320 101 440 160 522 242" fill="none" stroke="#fff" stroke-width="3"/>
      <path d="M0 392 C80 425 170 440 270 440 V555 H0 Z" fill="#e6e8eb"/>
      <path d="M0 390 C80 422 170 436 270 437" fill="none" stroke="url(#bottomBand)" stroke-width="8"/>
      <rect x="0" y="430" width="270" height="125" fill="url(#globePhoto)" opacity=".85" role="img" aria-label="Hand holding a glowing globe of media screens"/>
      <rect x="270" y="462" width="252" height="93" fill="url(#redBand)"/>
      <line x1="270" y1="120" x2="270" y2="555" stroke="#ddd" stroke-width="1"/>
    </svg>

    <div class="portal-mark">
      <div class="portal-mark__name">PRVN.com</div>
      <div class="portal-mark__tag">Provincial Applications Made Simple</div>
      <div class="portal-mark__note">Property of OTRV Consulting Group</div>
    </div>

    <article class="about">
      <h2 class="about__title">PRVN.COM</h2>
      <p>PRVN.com is an online application portal that allows OTRV to use reverse logistics to know where workers applications are at during the process. It is a streamlined system that works in coordination with the new PRVN and federal online applications.</p>
      <p>PRVN.com allows foreigner workers to upload their required documents for the application process as well as access information needed through our OTRV professional staff.</p>
      <p>Through live support OTRV's staff can communicate with workers in real time to answer questions from anywhere in the world and speed up application preparation for quicker submissions.</p>
      <p>The goal of PRVN.com is to be able to give businesses clients the advantage of an accurate assessments and updates of when workers can arrive to work at their business.</p>
      <div class="about__visit">Visit: www.prvn.com</div>
    </article>

    <div class="brand brand--mid">OTRV</div>

    <div class="contact">
      <h3 class="contact__title">OTRV –<br>“Overseas Talent &amp; Residency Ventures”</h3>
      <ul class="contact__list">
        <li>
          <svg width="8" height="11" viewBox="0 0 8 11"><path d="M4 0a4 4 0 0 1 4 4c0 3-4 7-4 7S0 7 0 4a4 4 0 0 1 4-4z" fill="var(--red)"/><circle cx="4" cy="4" r="1.5" fill="#fff"/></svg>
          <span>410-118 Birch Ave S.<br>Riverton, Saskatchewan<br>S4X-1A2</span>
        </li>
        <li class="contact__phones">
          <span><svg width="9" height="9" viewBox="0 0 9 9"><path d="M2 0l2 2-1 1.5 2.5 2.5L7 5l2 2-1.5 2C4 9 0 5 0 1.5z" fill="var(--red)"/></svg>306-555-0142</span>
          <span><svg width="9" height="9" viewBox="0 0 9 9"><path d="M2 0l2 2-1 1.5 2.5 2.5L7 5l2 2-1.5 2C4 9 0 5 0 1.5z" fill="var(--red)"/></svg>306-555-0187</span>
        </li>
        <li>
          <svg width="10" height="8" viewBox="0 0 10 8" style="margin-top:2px"><rect width="10" height="8" rx="1" fill="var(--red)"/><path d="M0 1l5 3.5L10 1" fill="none" stroke="#fff" stroke-width="1"/></svg>
          <span>info@otrv.ca</span>
        </li>
      </ul>
    </div>

    <ul class="links">
      <li>www.otrv.ca</li>
      <li>www.prvn.com</li>
      <li class="wide">www.northjobcafe.ca</li>
    </ul>
  </section>

  <section class="panel panel--cover">
    <svg class="art" width="258" height="555" viewBox="0 0 258 555">
      <defs>
        <linearGradient id="coverBlue" x1="0" y1="0" x2="0" y2="1">
          <stop offset="0" stop-color="#2f86dc"/>
          <stop offset="1" stop-color="#1450a0"/>
        </linearGradient>
        <radialGradient id="deskPhoto" cx=".5" cy=".45" r=".6">
          <stop offset="0" stop-color="#d9d9d9"/>
          <stop offset=".6" stop-color="#6b6b6b"/>
          <stop offset="1" stop-color="#1e1e1e"/>
        </radialGradient>
      </defs>
      <rect x="0" y="118" width="258" height="170" fill="var(--grey)" opacity=".6" role="img" aria-label="Faint world map"/>
      <path d="M0 290 C80 320 180 320 258 280 V555 H0 Z" fill="url(#coverBlue)"/>
      <circle cx="123" cy="262" r="130" fill="var(--red)"/>
      <circle cx="123" cy="262" r="122" fill="#fff"/>
      <circle cx="123" cy="262" r="118" fill="url(#deskPhoto)" role="img" aria-label="Businessman at a desk holding a glass globe"/>
      <path d="M0 380 C80 405 180 400 258 355 V555 H0 Z" fill="url(#coverBlue)"/>
    </svg>

    <div class="brand brand--cover">OTRV</div>

    <div class="cover-copy">
      <h1 class="cover-copy__title">TAKE A STEP WITH OTRV</h1>
      <p class="cover-copy__sub">– Overseas Talent<br>&amp; Residency Ventures</p>
      <p class="cover-copy__url">www.otrv.ca</p>
    </div>
  </section>

</main>
</body>
</html>
```